Business Card Design Project

Roofing Consultant firm needs business card design

R.T. Falkner & Co., Inc
Roofing Consultants and Contractors
Specializing in Construction Defect Litigation

4817 Willow Bend Ct.
San Diego, CA 92340
Licences:
CA 503274, AZ 927416, NV 0081532
www.rtfalkner-example.com

Will need cards for 3 persons:
Robert T. Falkner - Principal Consultant
Gordon Bleake - Associate Expert
Tessa Varnum - Controller
ph-555-274-1600
fax -555-274-1602
Cell - (will be 3 different numbers)
Email - (will be 3 different addresses)
Attached graphic is what we had before..the RTF with the roof graphic has been our logo for awhile, but we are open to change.
Updates

I now see we will need to add an email field to the design.  Sorry I didnt think of it when I was setting this up.  Thank you for your submittals. They are all very good. 

Target Market(s)

Attorneys, Homeowner Associations, Insurance Carriers

Industry/Entity Type

Business

Requirements
Must have
• RTF logo roof design. (owner created)

```html
<!DOCTYPE html>
<html lang="en">
<head>
<meta charset="utf-8">
<title>R.T. Falkner &amp; Co. Inc — Business Card</title>
<link rel="stylesheet" href="https://fonts.googleapis.com/css2?family=Cutive+Mono&display=swap">
<style>
  :root {
    --paper: #ffffff;
    --ink: #231f20;
    --frame: #a7a7a7;
    --type: "Cutive Mono", "Courier New", monospace;
  }
  html, body {
    margin: 0;
    padding: 0;
    width: 1200px;
    height: 900px;
    overflow: hidden;
    background: var(--paper);
  }
  .card {
    position: absolute;
    left: 73px;
    top: 150px;
    width: 1047px;
    height: 594px;
    border: 3px solid var(--frame);
    background: var(--paper);
    color: var(--ink);
    font-family: var(--type);
  }
  .card p { margin: 0; position: absolute; white-space: nowrap; }
  .company {
    left: 68px; top: 30px;
    font-size: 39px;
    letter-spacing: 1px;
  }
  .company-rule {
    position: absolute;
    left: 68px; top: 82px;
    width: 558px; height: 2px;
    background: var(--ink);
  }
  .tagline {
    left: 68px; top: 90px;
    font-size: 37px;
    line-height: 44px;
    letter-spacing: 1px;
  }
  .brand-name {
    right: 60px; top: 250px;
    font-size: 84px;
    letter-spacing: 2px;
  }
  .firm-details {
    right: 40px; top: 440px;
    text-align: right;
    font-size: 17px;
    line-height: 24px;
  }
  .person-name {
    left: 68px; top: 410px;
    font-size: 28px;
    letter-spacing: 1px;
  }
  .person-title {
    left: 68px; top: 446px;
    font-size: 28px;
    letter-spacing: 1px;
  }
  .person-rule {
    position: absolute;
    left: 72px; top: 492px;
    width: 276px; height: 1px;
    background: var(--ink);
  }
  .contacts {
    left: 68px; top: 498px;
    font-size: 19px;
    line-height: 22px;
  }
</style>
</head>
<body>
  <main class="card">
    <p class="company">R.T. Falkner &amp; Co. Inc</p>
    <div class="company-rule"></div>
    <p class="tagline">Roofing Consultants and<br>Contractors</p>

    <p class="brand-name">RTF</p>

    <p class="firm-details">4817 Willow Bend Ct.<br>San Diego, CA 92340<br>Lic. CA 503274 · AZ 927416 · NV 0081532<br>www.rtfalkner-example.com</p>

    <p class="person-name">Gordon Bleake</p>
    <p class="person-title">Associate Expert</p>
    <div class="person-rule"></div>
    <p class="contacts">c/555.555.555<br>ph/555.274.1600<br>fax/555.274.1602<br>e/gbleake@rtfalkner-example.com</p>
  </main>
</body>
</html>
```